Mine Engineering Consultancy specializing in
* Pit optimization
* Mine Design
* Scheduling
* Mine Rehabilitation

Industry/Entity Type

Mining

Contact Information for Business Card

RVT Mining Pty Ltd
Derek Holloway
Director/Principle Mining Engineer
Mobile 0413582961
Email derek.holloway@rvtmining-example.com

```html
<!DOCTYPE html>
<html lang="en">
<head>
<meta charset="utf-8">
<title>RVT Mining Pty Ltd – Business Card</title>
<link rel="stylesheet" href="https://fonts.googleapis.com/css2?family=Open+Sans:wght@400;600;700;800&family=Merriweather:wght@400&display=swap">
<style>
  :root {
    --page-bg: #e9eaec;
    --front-blue-light: #6583b0;
    --front-blue-dark: #47679a;
    --back-grey-light: #f1f1f1;
    --back-grey-dark: #d4d5d7;
    --brand-blue: #1f6fc0;
    --text-dark: #1c1c1c;
    --white: #ffffff;
    --rule: #8a8f96;
  }
  * { box-sizing: border-box; margin: 0; padding: 0; }
  html, body { width: 1200px; height: 864px; overflow: hidden; }
  body {
    background: var(--page-bg);
    font-family: "Open Sans", Arial, sans-serif;
    position: relative;
  }
  .card {
    position: absolute;
    left: 302px;
    width: 596px;
    height: 340px;
    overflow: hidden;
    box-shadow: 0 2px 6px rgba(0,0,0,0.12);
  }
  .card-front { top: 66px; }
  .card-back { top: 458px; }

  .card-backdrop { position: absolute; inset: 0; }
  .card-front .card-backdrop {
    background: linear-gradient(160deg, var(--front-blue-light) 0%, var(--front-blue-dark) 100%);
  }
  .card-back .card-backdrop {
    background: linear-gradient(160deg, var(--back-grey-light) 0%, var(--back-grey-dark) 100%);
  }

  /* Front */
  .front-wordmark {
    position: absolute;
    top: 40px; left: 0; right: 0;
    text-align: center;
    color: var(--white);
    font-weight: 800;
    font-size: 132px;
    line-height: 1;
    letter-spacing: 4px;
  }
  .services {
    position: absolute;
    top: 212px; left: 0; right: 0;
    text-align: center;
    color: var(--white);
    font-size: 14px;
    line-height: 22px;
  }
  .services .dot {
    display: inline-block;
    width: 8px; height: 8px;
    border-radius: 50%;
    background: var(--white);
    margin: 0 7px;
    vertical-align: 1px;
  }

  /* Back */
  .brand-lockup {
    position: absolute;
    top: 86px; left: 96px;
    display: flex;
    align-items: center;
  }
  .back-wordmark {
    color: var(--brand-blue);
    font-weight: 800;
    font-size: 54px;
    line-height: 1;
    letter-spacing: 2px;
  }
  .lockup-rule {
    width: 1px; height: 52px;
    background: var(--rule);
    margin: 0 18px 0 20px;
  }
  .company-suffix {
    font-family: "Merriweather", Georgia, serif;
    color: var(--brand-blue);
    font-size: 26px;
    margin-top: 22px;
  }
  .person {
    position: absolute;
    left: 40px; top: 200px;
  }
  .person-name {
    color: var(--brand-blue);
    font-weight: 700;
    font-size: 18px;
  }
  .person-title {
    color: var(--text-dark);
    font-size: 13.5px;
    margin-top: 2px;
  }
  .contact-list {
    position: absolute;
    right: 26px; top: 262px;
    list-style: none;
    text-align: right;
    color: var(--text-dark);
    font-size: 14px;
  }
  .contact-list li {
    display: flex;
    align-items: center;
    justify-content: flex-end;
    height: 24px;
  }
  .contact-icon {
    width: 18px; height: 16px;
    margin-left: 8px;
    background: var(--brand-blue);
    border-radius: 2px;
    display: flex; align-items: center; justify-content: center;
  }
</style>
</head>
<body>
  <section class="card card-front">
    <div class="card-backdrop" role="img" aria-label="Blue-toned aerial photograph of an open-pit mine"></div>
    <div class="front-wordmark">RVT</div>
    <p class="services">
      Pit optimization<span class="dot"></span>Mine Design<span class="dot"></span>Scheduling<br>
      Mine Rehabilitation
    </p>
  </section>

  <section class="card card-back">
    <div class="card-backdrop" role="img" aria-label="Faded grey aerial photograph of an open-pit mine"></div>
    <div class="brand-lockup">
      <span class="back-wordmark">RVT</span>
      <span class="lockup-rule"></span>
      <span class="company-suffix">Mining Pty Ltd</span>
    </div>
    <div class="person">
      <p class="person-name">Derek Holloway</p>
      <p class="person-title">Director/Principle Mining Engineer</p>
    </div>
    <ul class="contact-list">
      <li>0413582961
        <span class="contact-icon">
          <svg width="12" height="10" viewBox="0 0 12 10" aria-hidden="true">
            <path d="M1 3 Q6 0 11 3 L9.5 4.5 L8 3.3 L4 3.3 L2.5 4.5 Z" fill="#fff"/>
            <rect x="2.5" y="5" width="7" height="4" rx="1" fill="#fff"/>
          </svg>
        </span>
      </li>
      <li>derek.holloway@rvtmining-example.com
        <span class="contact-icon">
          <svg width="12" height="9" viewBox="0 0 12 9" aria-hidden="true">
            <rect x="0.5" y="0.5" width="11" height="8" fill="#fff"/>
            <path d="M0.5 0.5 L6 5 L11.5 0.5" fill="none" stroke="#1f6fc0" stroke-width="1"/>
          </svg>
        </span>
      </li>
    </ul>
  </section>
</body>
</html>
```